Graphic Design for Ad Tracking Software

Leading software for home business that helps identify which traffic sources have the highest ROI. Industry rated #1, been in business for 10 years.

```html
<!DOCTYPE html>
<html lang="en">
<head>
<meta charset="utf-8">
<title>Ad Tracking Software</title>
<link rel="stylesheet" href="https://fonts.googleapis.com/css2?family=Arimo:wght@400;700&display=swap">
<style>
:root{
  --ribbon:#c6cdf6;
  --ribbon-line:#1a1a2a;
  --nav-bg:#eef0f1;
  --nav-text:#3a9ccc;
  --title:#2a8fd0;
  --body:#3a3a3a;
  --link:#1c8ad6;
  --pill-top:#3fb0f3;
  --pill-bottom:#0781d6;
  --arrow:#1a7fd0;
  --panel-line:#d8dde2;
  --bg:#ffffff;
}
*{margin:0;padding:0;box-sizing:border-box}
html,body{width:1200px;height:900px;overflow:hidden;background:var(--bg)}
body{font-family:"Arimo",Arial,sans-serif;color:var(--body);position:relative}
.banner{position:absolute;left:0;top:0;width:1200px;height:92px}
.banner-title{position:absolute;left:300px;top:0;width:600px;height:88px;display:flex;align-items:center;justify-content:center;font-size:29px;font-weight:700;color:#000}
.nav{position:absolute;left:0;top:93px;width:1195px;height:27px;background:var(--nav-bg);border-bottom:1px solid var(--panel-line)}
.nav span{position:absolute;top:5px;transform:translateX(-50%);font-size:15px;color:var(--nav-text);white-space:nowrap}
.panel{position:absolute;left:0;top:120px;width:1195px;height:510px;border-right:1px solid var(--panel-line);border-bottom:1px solid var(--panel-line)}
.panel h1{position:absolute;left:22px;top:30px;font-size:28px;font-weight:700;color:var(--title)}
.intro{position:absolute;left:22px;top:84px;width:1165px;font-size:14px;line-height:16.5px;color:var(--body)}
.feature{position:absolute;display:flex;align-items:flex-start;gap:14px}
.feature svg{flex:none}
.feature h2{font-size:17px;font-weight:700;color:var(--link);margin-top:6px}
.feature p{font-size:14px;line-height:16px;color:var(--body)}
.diagram{position:absolute;left:0;top:640px;width:1200px;height:260px}
.pill{position:absolute;height:32px;border-radius:16px;background:linear-gradient(var(--pill-top),var(--pill-bottom));color:#fff;font-weight:700;font-size:14px;letter-spacing:1.5px;display:flex;align-items:center;justify-content:center}
.hub{position:absolute;left:409px;top:103px;width:390px;height:68px;border-radius:6px;background:linear-gradient(var(--pill-top),var(--pill-bottom));color:#fff;font-weight:700;font-size:24px;letter-spacing:1.5px;display:flex;align-items:center;justify-content:center}
.arrows{position:absolute;left:0;top:0}
</style>
</head>
<body>

<svg class="banner" viewBox="0 0 1200 92">
  <path d="M0 0 H300 V80 H0 L60 40 Z" fill="var(--ribbon)" stroke="var(--ribbon-line)" stroke-width="1.5"/>
  <path d="M1200 0 H900 V80 H1200 L1140 40 Z" fill="var(--ribbon)" stroke="var(--ribbon-line)" stroke-width="1.5"/>
  <path d="M300 2 Q600 -6 900 2 V86 Q600 94 300 86 Z" fill="var(--ribbon)" stroke="var(--ribbon-line)" stroke-width="1.5"/>
</svg>
<div class="banner-title">Ad Tracking Software</div>

<nav class="nav">
  <span style="left:180px">Campaign Management</span>
  <span style="left:401px">Statistics</span>
  <span style="left:583px">Split Testing</span>
  <span style="left:760px">Cloaking</span>
  <span style="left:920px">System</span>
  <span style="left:1072px">Manual</span>
</nav>

<section class="panel">
  <h1>Adminstration Area</h1>
  <p class="intro">At first create a New Campaign. A tracking link will be supplied to you which you can publish in your ads. Instead of sending your visitors to examplehome.site, you can send them to your new tracking link. Everytime somebody clicks on your tracking link, the tracking software will record the hit and send the visitor to examplehome.site, or whatever destination url you want to send them to. When done add the tracking codes to your website. The Conversion Tracking section generates the html code required to track sales or actions on your website. Some examples of an action is a subcription, or a request to download a free version of your product.</p>

  <div class="feature" style="left:118px;top:210px">
    <svg width="62" height="62" viewBox="0 0 62 62"><circle cx="31" cy="31" r="30" fill="#bfe3fb"/><circle cx="31" cy="31" r="24" fill="#2d9be6"/><rect x="22" y="24" width="18" height="14" rx="2" fill="#fff"/></svg>
    <div><h2>New Campaign</h2><p>Create a New Campaign</p></div>
  </div>
  <div class="feature" style="left:430px;top:210px">
    <svg width="62" height="62" viewBox="0 0 62 62"><circle cx="31" cy="31" r="30" fill="#bfe3fb"/><circle cx="31" cy="31" r="24" fill="#2d9be6"/><rect x="23" y="21" width="16" height="20" rx="2" fill="#fff"/></svg>
    <div><h2>Campaign Management</h2><p>Edit and Delete Campaigns<br>and Reset Hits</p></div>
  </div>
  <div class="feature" style="left:766px;top:210px">
    <svg width="62" height="62" viewBox="0 0 62 62"><circle cx="31" cy="31" r="30" fill="#bfe3fb"/><circle cx="31" cy="31" r="24" fill="#2d9be6"/><rect x="22" y="30" width="5" height="10" fill="#fff"/><rect x="29" y="24" width="5" height="16" fill="#fff"/><rect x="36" y="27" width="5" height="13" fill="#fff"/></svg>
    <div><h2>Statistics Overview</h2><p>Check your Conversion Rate<br>and Traffic Statistics</p></div>
  </div>

  <div class="feature" style="left:118px;top:307px">
    <svg width="62" height="62" viewBox="0 0 62 62"><circle cx="31" cy="31" r="30" fill="#bfe3fb"/><circle cx="31" cy="31" r="24" fill="#2d9be6"/><rect x="27" y="20" width="8" height="7" fill="#fff"/><rect x="19" y="35" width="8" height="7" fill="#fff"/><rect x="35" y="35" width="8" height="7" fill="#fff"/><path d="M31 27 V31 H23 V35 M31 31 H39 V35" stroke="#fff" stroke-width="2" fill="none"/></svg>
    <div><h2>Split Testing</h2><p>Test which Salespage<br>converts better</p></div>
  </div>
  <div class="feature" style="left:430px;top:307px">
    <svg width="62" height="62" viewBox="0 0 62 62"><circle cx="31" cy="31" r="30" fill="#bfe3fb"/><circle cx="31" cy="31" r="24" fill="#2d9be6"/><rect x="21" y="23" width="20" height="15" rx="2" fill="#fff"/></svg>
    <div><h2>Link Cloaking</h2><p>Protect your Affiliate<br>Commission</p></div>
  </div>
  <div class="feature" style="left:766px;top:307px">
    <svg width="62" height="62" viewBox="0 0 62 62"><circle cx="31" cy="31" r="30" fill="#bfe3fb"/><circle cx="31" cy="31" r="24" fill="#2d9be6"/><rect x="21" y="23" width="20" height="16" rx="2" fill="#fff"/><path d="M24 28 H38 M24 33 H34" stroke="#2d9be6" stroke-width="2"/></svg>
    <div><h2>Keyword Tracking</h2><p>Track your campaigns on<br>keyword level</p></div>
  </div>

  <div class="feature" style="left:118px;top:405px">
    <svg width="62" height="62" viewBox="0 0 62 62"><circle cx="31" cy="31" r="30" fill="#bfe3fb"/><circle cx="31" cy="31" r="24" fill="#2d9be6"/><path d="M22 31 L28 37 L40 24" stroke="#fff" stroke-width="4" fill="none" stroke-linecap="round"/></svg>
    <div><h2>Conversion Tracking</h2><p>Track Sales, Leads and<br>Actions</p></div>
  </div>
  <div class="feature" style="left:430px;top:405px">
    <svg width="62" height="62" viewBox="0 0 62 62"><circle cx="31" cy="31" r="30" fill="#bfe3fb"/><circle cx="31" cy="31" r="24" fill="#2d9be6"/><rect x="24" y="20" width="15" height="21" rx="1" fill="#fff"/><path d="M27 26 H36 M27 30 H36 M27 34 H33" stroke="#2d9be6" stroke-width="1.5"/></svg>
    <div><h2>PPC Landing Page</h2><p>Create a PPC Landing Page</p></div>
  </div>
  <div class="feature" style="left:766px;top:405px">
    <svg width="62" height="62" viewBox="0 0 62 62"><circle cx="31" cy="31" r="30" fill="#bfe3fb"/><circle cx="31" cy="31" r="24" fill="#2d9be6"/><path d="M21 31 H35 M30 25 L37 31 L30 37" stroke="#fff" stroke-width="4" fill="none" stroke-linecap="round" stroke-linejoin="round"/></svg>
    <div><h2>Export Statistics</h2><p>Export Campaign Statistics<br>Reports</p></div>
  </div>
</section>

<section class="diagram">
  <svg class="arrows" width="1200" height="260" viewBox="0 0 1200 260">
    <defs>
      <marker id="head" viewBox="0 0 10 10" refX="9" refY="5" markerWidth="7" markerHeight="7" orient="auto">
        <path d="M0 0 L10 5 L0 10 Z" fill="var(--arrow)"/>
      </marker>
    </defs>
    <g stroke="var(--arrow)" stroke-width="2" marker-end="url(#head)">
      <line x1="180" y1="50" x2="400" y2="102"/>
      <line x1="460" y1="50" x2="510" y2="98"/>
      <line x1="700" y1="50" x2="690" y2="98"/>
      <line x1="1010" y1="50" x2="810" y2="102"/>
      <line x1="305" y1="133" x2="403" y2="133"/>
      <line x1="892" y1="136" x2="805" y2="136"/>
      <line x1="190" y1="222" x2="400" y2="172"/>
      <line x1="460" y1="222" x2="510" y2="176"/>
      <line x1="730" y1="222" x2="690" y2="176"/>
      <line x1="1050" y1="222" x2="810" y2="172"/>
    </g>
  </svg>

  <div class="pill" style="left:19px;top:16px;width:285px">BANNERS</div>
  <div class="pill" style="left:311px;top:16px;width:289px">POPUPS</div>
  <div class="pill" style="left:603px;top:16px;width:284px">EMAIL ADS</div>
  <div class="pill" style="left:893px;top:16px;width:287px">CLASSIFIED ADS</div>

  <div class="pill" style="left:16px;top:116px;width:288px">PPC SEARCH ENGINES</div>
  <div class="hub">Your Website</div>
  <div class="pill" style="left:893px;top:120px;width:287px">SEARCH ADS</div>

  <div class="pill" style="left:19px;top:223px;width:285px">PRESS RELEASES</div>
  <div class="pill" style="left:311px;top:223px;width:289px">ARTICLES</div>
  <div class="pill" style="left:603px;top:223px;width:284px">FORUMS</div>
  <div class="pill" style="left:893px;top:223px;width:287px">LINKS</div>
</section>

</body>
</html>
```